Corvelle Beauty Lounge needs a product poster

This poster is advertising our products and services. There are several damask patterns throughout the store. Our store's colors are blue, yellow, white, and gold.However the use of vibrant colors would be great! Our theme is old Hollywood. We have to use this design for our price list, product advertisement, and store promotions poster. Poster 2 and 3 can have the same layout. Poster 1 is different because I want the menu enclosed in a frame with the model resting against it or on top of it. All three posters will be hung on the same wall. I have attached my logo and additional photos for your review. I have also attached a images few posters. To give a better idea. I like how the fonts are not all the same. I like how they used the space. I like the use of color. Also I want the logo small with a white oval background. I don't want our logo to be a focal point.
Poster 1: The menu. This poster should include the blonde sailor either above the menu or beside the menu, 2 images have been included to choose from. I want the area with the prices in some type of decorative frame, with the model on top or on the side. (The model is displaying the prices) Also the model's background is white but I want her background to have color. Green would be great! I also like the idea of having "Now Showing" as part of the frame.
The text should read
" Services
Full Body Application..........................................$35.00
Half Body Application.........................................$20.00
Competition Application......................................$50,00
Face Only...........................................................$10.00
Packages:
4 Tans.... ............................................................$120.00 (Never Expires)
8 Tans ................................................................$200.00 (Never Expires)
Monthly Unlimited...............................................$95.00
Specials:
High School Students .......................................$25.00 EVERYDAY!!
All Day Every Tuesday.......................................$25.00
New Clients........................................................$25.00 (First Visit Only)
(If you want to be creative this section can be separate from the menu or part of the menu. Your choice)
Don't have time to come to us? We also have MOBILE Services! OUR ARTISTS CAN COME TO YOU!
In-Home Party Rates (5 people or more)...........$35.00 per person (Travel Fee Waived)
Poster 2: Kelvane Solution...The image of the pinup with the clock if for this poster.
The text should read:
" PRESSED FOR TIME? Try our KELVANE sunless solution. Rinse in as little as 2 hours" (Pressed for time, Kelvane, and 2 Hours is what we want to stand out)
Poster 3: Packages..The image for this poster is of the girl with the binoculars.
The text should read:
"We offer packages and memberships with UNBELIEVABLE SAVINGS. Tans as low as $20!!" (Unbelievable savings and $20 is what we want to stand out)
I made changes to my briefing. Please let me know if I need to make any other changes or additions
We increased our budget for our design, in order to get more participants
I updated our brief. I have included examples and more detailed instructions. I hope this helps
People who value beauty and glamour. We have an upscale clientele.
Advertising

```html
<!DOCTYPE html>
<html lang="en">
<head>
<meta charset="utf-8">
<title>Corvelle Beauty Lounge – Packages Poster</title>
<link rel="stylesheet" href="https://fonts.googleapis.com/css2?family=Righteous&family=Stardos+Stencil:wght@700&display=swap">
<style>
  :root {
    --paper-light: #f3b8a8;
    --paper-mid: #e8968a;
    --paper-dark: #d97c72;
    --model-denim: #6f88ad;
    --model-dress: #c9cfd8;
    --model-skin: #e2a98e;
    --panel-red: #d5302b;
    --panel-red-deep: #bf2522;
    --cream: #f6ecdc;
    --gold: #f2c23a;
    --gold-outline: #3d7cc6;
    --band-blue: #3a70b9;
    --band-stripe: #dfe7f1;
    --oval-white: #ffffff;
    --logo-ink: #6a3a8e;
  }
  html, body {
    margin: 0;
    padding: 0;
    width: 1200px;
    height: 960px;
    overflow: hidden;
    background: #ffffff;
  }
  .poster {
    position: relative;
    width: 1200px;
    height: 960px;
    overflow: hidden;
    font-family: "Righteous", sans-serif;
  }
  .paper-backdrop {
    position: absolute;
    left: 0;
    top: 0;
    width: 875px;
    height: 837px;
    background: radial-gradient(ellipse at 40% 35%, var(--paper-light) 0%, var(--paper-mid) 55%, var(--paper-dark) 100%);
  }
  .model-photo {
    position: absolute;
    left: 20px;
    top: 24px;
    width: 690px;
    height: 813px;
    border-radius: 46% 40% 8% 8% / 30% 30% 4% 4%;
    background: linear-gradient(180deg, var(--model-skin) 0%, var(--model-denim) 38%, var(--model-dress) 70%, var(--model-dress) 100%);
    opacity: 0.85;
  }
  .offer-panel {
    position: absolute;
    left: 875px;
    top: 0;
    width: 325px;
    height: 837px;
    background: linear-gradient(180deg, var(--panel-red) 0%, var(--panel-red-deep) 100%);
  }
  .offer-copy {
    position: absolute;
    right: 21px;
    margin: 0;
    text-align: right;
    white-space: nowrap;
    line-height: 1;
  }
  .offer-copy--lead {
    color: var(--cream);
    font-family: "Righteous", sans-serif;
  }
  .line-we-offer { top: 90px; font-size: 44px; letter-spacing: 14px; margin-right: -14px; }
  .line-packages { top: 145px; font-size: 42px; letter-spacing: 1px; margin-right: -1px; }
  .line-memberships { top: 203px; font-size: 42px; letter-spacing: 3px; margin-right: -3px; }
  .line-with { top: 274px; font-size: 50px; letter-spacing: 50px; margin-right: -50px; }
  .line-tans { top: 600px; font-size: 41px; }

  .offer-copy--highlight {
    font-family: "Stardos Stencil", serif;
    font-weight: 700;
    color: var(--gold);
    -webkit-text-stroke: 3px var(--gold-outline);
    paint-order: stroke fill;
  }
  .line-unbelievable { top: 381px; font-size: 70px; transform: scaleX(0.82); transform-origin: right center; }
  .line-savings { top: 466px; font-size: 100px; }
  .line-price { top: 664px; font-size: 175px; }

  .brand-band {
    position: absolute;
    left: 0;
    top: 837px;
    width: 1200px;
    height: 123px;
    background: var(--band-blue);
  }
  .brand-band__stripe {
    position: absolute;
    left: 0;
    top: 48px;
    width: 100%;
    height: 21px;
    background: var(--band-stripe);
  }
  .brand-mark {
    position: absolute;
    left: 37px;
    top: 22px;
    width: 188px;
    height: 80px;
    border-radius: 50%;
    background: var(--oval-white);
    display: flex;
    align-items: center;
    justify-content: center;
    text-align: center;
  }
  .brand-mark__name {
    font-family: "Righteous", sans-serif;
    font-size: 17px;
    line-height: 1.05;
    color: var(--logo-ink);
  }
</style>
</head>
<body>
  <main class="poster">
    <div class="paper-backdrop"></div>
    <div class="model-photo" role="img" aria-label="Retro pin-up model in a denim and floral dress looking through binoculars while holding an open laptop"></div>

    <section class="offer-panel" aria-label="Packages offer"></section>

    <p class="offer-copy offer-copy--lead line-we-offer">we offer</p>
    <p class="offer-copy offer-copy--lead line-packages">packages and</p>
    <p class="offer-copy offer-copy--lead line-memberships">memberships</p>
    <p class="offer-copy offer-copy--lead line-with">with</p>
    <p class="offer-copy offer-copy--highlight line-unbelievable">UNBELIEVABLE</p>
    <p class="offer-copy offer-copy--highlight line-savings">SAVINGS</p>
    <p class="offer-copy offer-copy--lead line-tans">tans as low as</p>
    <p class="offer-copy offer-copy--highlight line-price">$20</p>

    <footer class="brand-band">
      <div class="brand-band__stripe"></div>
      <div class="brand-mark">
        <span class="brand-mark__name">Corvelle<br>Beauty Lounge</span>
      </div>
    </footer>
  </main>
</body>
</html>
```